Business Card Design

Larkfield Valley Care Homes, Inc. (LVCH, Inc.) is a private, non-profit corporation which provides an array of services to individuals in a community setting. These services include residential, vocational/day, and therapeutic recreation that afford individuals the opportunity to integrate into the community and participate as valued members of society. We work with individuals with developmental disabilities, traumatic brain injury and the elderly. We are a very small company with approximately 100 employees. We have been in business since 1975. We are looking for a business card that is professional, trendy and little out of the box. The Executive Director likes colors that are in the blue or green family. Open to add other colors to the design. The business card needs to include a house. We currently have a design on our old webpage that he likes. The webpage is larkfieldvalleycarehomes.org. He likes that a lot. There is also a picture on our Facebook page that someone drew that he likes. This will be the business card for our entire agency. All administrative staff in our agency will have the same business card but have their information plugged in.

Industry/Entity Type

Non-Profit

Contact Information for Business Card

For questions you will need to contact me, Marlene Tobisch at 555-284-7730 ext. 214. The information below will be used for the business card:

Gordon Hallbeck, Executive Director
Larkfield Valley Care Homes, Inc.
418 W. Elm Avenue - PO Box 386
Harlow Springs, VA 24590
gordon.hallbeck@lvchinc.org
555-284-7730 - work
555-631-0982 - cell
555-284-5167 - fax

Requirements
Must have
• I am really open when it comes to design. The only design that must be included is a house

```html
<!DOCTYPE html>
<html lang="en">
<head>
<meta charset="utf-8">
<title>Larkfield Valley Care Homes, Inc. — Business Card</title>
<link rel="stylesheet" href="https://fonts.googleapis.com/css2?family=Bebas+Neue&family=Montserrat:ital,wght@0,300;0,400;0,600;1,300&display=swap">
<style>
  :root {
    --card-red: #b80e14;
    --paper: #ffffff;
    --ink: #111111;
    --icon-disc: #0c0c0c;
  }
  * { box-sizing: border-box; margin: 0; padding: 0; }
  html, body { width: 702px; height: 1200px; overflow: hidden; background: var(--paper); }
  .card {
    position: relative;
    width: 702px;
    height: 1200px;
    background: var(--paper);
    font-family: "Montserrat", sans-serif;
    color: var(--ink);
    overflow: hidden;
  }
  .brand {
    position: absolute;
    top: 148px;
    left: 0;
    width: 100%;
    display: flex;
    justify-content: center;
    align-items: center;
    gap: 18px;
  }
  .brand-mark {
    width: 46px;
    height: 46px;
    background: var(--card-red);
    flex: none;
  }
  .brand-name {
    font-family: "Montserrat", sans-serif;
    font-weight: 600;
    font-size: 30px;
    line-height: 1.15;
    color: var(--ink);
    max-width: 360px;
  }
  .tagline {
    position: absolute;
    top: 296px;
    left: 0;
    width: 100%;
    text-align: center;
    font-style: italic;
    font-weight: 300;
    font-size: 22px;
    line-height: 31px;
    color: var(--card-red);
  }
  .person-name {
    position: absolute;
    top: 474px;
    left: 0;
    width: 100%;
    text-align: center;
    font-family: "Bebas Neue", sans-serif;
    font-weight: 400;
    font-size: 63px;
    letter-spacing: 1px;
    line-height: 1;
    color: var(--card-red);
  }
  .person-title {
    position: absolute;
    top: 546px;
    left: 0;
    width: 100%;
    text-align: center;
    font-weight: 300;
    font-size: 27px;
    letter-spacing: 1px;
    color: var(--ink);
  }
  .contact-band {
    position: absolute;
    left: 0;
    top: 0;
    width: 702px;
    height: 1200px;
  }
  .contact-list {
    position: absolute;
    left: 0;
    top: 684px;
    width: 100%;
    list-style: none;
    text-align: center;
    color: var(--paper);
    font-weight: 300;
    font-size: 24px;
    line-height: 32px;
  }
  .contact-item { display: flex; flex-direction: column; align-items: center; min-height: 87px; }
  .contact-icon { width: 32px; height: 32px; flex: none; }
  .contact-text { flex: none; }
</style>
</head>
<body>
<main class="card">
  <svg class="contact-band" viewBox="0 0 702 1200" aria-hidden="true">
    <polygon points="0,752 349,612 702,752 702,1200 0,1200" fill="var(--card-red)"/>
  </svg>

  <header class="brand">
    <span class="brand-mark"></span>
    <span class="brand-name">Larkfield Valley Care Homes, Inc.</span>
  </header>

  <p class="tagline">Providing specialized services to persons<br>with disabilities since 1975</p>

  <h1 class="person-name">Gordon Hallbeck</h1>
  <p class="person-title">EXECUTIVE DIRECTOR</p>

  <ul class="contact-list">
    <li class="contact-item">
      <svg class="contact-icon" viewBox="0 0 32 32" aria-hidden="true">
        <circle cx="16" cy="16" r="16" fill="var(--icon-disc)"/>
        <rect x="8.5" y="10.5" width="15" height="11" rx="1.5" fill="none" stroke="var(--card-red)" stroke-width="1.8"/>
        <polyline points="9,11.5 16,17 23,11.5" fill="none" stroke="var(--card-red)" stroke-width="1.8"/>
      </svg>
      <span class="contact-text">gordon.hallbeck@lvchinc.org</span>
    </li>
    <li class="contact-item">
      <svg class="contact-icon" viewBox="0 0 32 32" aria-hidden="true">
        <circle cx="16" cy="16" r="16" fill="var(--icon-disc)"/>
        <path d="M11 8.5c1 0 2.6 3.2 2.6 4 0 .9-1.6 1.3-1.4 2.3.4 1.8 2.6 4.2 4.3 4.8 1 .3 1.5-1.3 2.4-1.3.8 0 3.8 1.8 3.8 2.8 0 1.4-2.2 3-3.8 2.8C13.5 23.3 8.5 17.6 8.4 12c0-1.6 1.3-3.5 2.6-3.5z" fill="var(--card-red)"/>
      </svg>
      <span class="contact-text">work 555-284-7730</span>
    </li>
    <li class="contact-item">
      <svg class="contact-icon" viewBox="0 0 32 32" aria-hidden="true">
        <circle cx="16" cy="16" r="16" fill="var(--icon-disc)"/>
        <rect x="10.5" y="6.5" width="11" height="19" rx="2" fill="var(--card-red)"/>
        <rect x="12.3" y="9" width="7.4" height="12.5" fill="var(--icon-disc)"/>
        <circle cx="16" cy="23.4" r="0.9" fill="var(--icon-disc)"/>
      </svg>
      <span class="contact-text">cell 555-631-0982</span>
    </li>
    <li class="contact-item">
      <svg class="contact-icon" viewBox="0 0 32 32" aria-hidden="true">
        <circle cx="16" cy="16" r="16" fill="var(--icon-disc)"/>
        <path d="M10 7h8.5l4 4v14h-12.5z" fill="var(--card-red)"/>
        <g stroke="var(--icon-disc)" stroke-width="1.4">
          <line x1="12.5" y1="14" x2="20" y2="14"/>
          <line x1="12.5" y1="17" x2="20" y2="17"/>
          <line x1="12.5" y1="20" x2="20" y2="20"/>
        </g>
      </svg>
      <span class="contact-text">fax 555-284-5167</span>
    </li>
    <li class="contact-item">
      <svg class="contact-icon" viewBox="0 0 32 32" aria-hidden="true">
        <circle cx="16" cy="16" r="16" fill="var(--icon-disc)"/>
        <path d="M16 7.5l9 8h-2.6v8h-4.4v-5h-4v5H9.6v-8H7z" fill="var(--card-red)"/>
      </svg>
      <span class="contact-text">418 W. Elm Avenue | PO Box 386<br>Harlow Springs, VA 24590</span>
    </li>
  </ul>
</main>
</body>
</html>
```